Wordpress website and end user portal (also Wordpress) design

We need a design overhaul for front end website and end user portal, both in Wordpress. See attachment or scope. Designer will provide:
1. Logo design options for us to select
2. Provide stock imagery where needed
3. Design end user portal pages with a slick and innovative look (no functionality, just design).
4. Use screen shots of end user portal after designing to use on website.
Approximately 8-10 website pages in design and design clean up on the end user pages. Will have scope and details in next 48 hours.
Requirements:
1. Wordpress experience
2. Creative mindset
3. Innovative design experience and application
Business Software
5+ page

```html
<!DOCTYPE html>
<html lang="en">
<head>
<meta charset="utf-8">
<title>TaskGrid360 – Business Software</title>
<link href="https://fonts.googleapis.com/css2?family=Poppins:wght@400;500;600;700;800&display=swap" rel="stylesheet">
<style>
:root{
  --blue:#1d5cf0;
  --blue-dark:#0f3fc4;
  --blue-soft:#e9effd;
  --green:#1f8a3e;
  --orange:#f6a623;
  --ink:#1e1f24;
  --muted:#7a7f8a;
  --line:#e3e6ec;
  --dark:#1c1d20;
  --white:#ffffff;
}
*{box-sizing:border-box;margin:0;padding:0}
html,body{width:1200px;height:4712px;overflow:hidden}
body{font-family:'Poppins',sans-serif;color:var(--ink);background:var(--white);position:relative}
.abs{position:absolute}
.center{text-align:center}
.btn{display:inline-block;font-size:11px;font-weight:600;text-transform:uppercase;color:var(--white);padding:10px 24px;border-radius:2px;letter-spacing:.3px}
.btn--blue{background:var(--blue)}
.btn--green{background:var(--green)}
.btn--orange{background:var(--orange)}
.btn--dark{background:#1b1c20}
.dot{width:10px;height:10px;border-radius:50%;background:var(--blue);margin:0 auto}
.section-title{font-size:30px;font-weight:700;color:var(--blue);text-transform:uppercase;text-align:center;width:1200px;left:0}

/* header / hero */
.hero{left:0;top:0;width:1200px;height:535px;background:linear-gradient(120deg,#3b3f46 0%,#8d8578 45%,#c9c0b2 70%,#6d6a66 100%)}
.hero__corner{left:0;top:0}
.nav{left:0;top:0;width:1200px;height:40px}
.brand{left:110px;top:10px;font-size:24px;font-weight:800;color:var(--white);display:flex;align-items:center;gap:8px}
.brand__mark{width:16px;height:16px;border-radius:50%;background:var(--white)}
.menu{left:650px;top:14px;display:flex;gap:22px;font-size:11px;color:var(--white);font-weight:500}
.menu__cta{left:1022px;top:9px;background:var(--green);color:#fff;font-size:10px;font-weight:600;padding:6px 10px}
.login{left:933px;top:44px;width:157px;height:146px;background:var(--white);box-shadow:0 4px 14px rgba(0,0,0,.25);padding:14px 12px}
.login__field{height:20px;border:1px solid var(--line);margin-bottom:8px}
.login__remember{font-size:8px;color:var(--muted);display:flex;align-items:center;gap:4px;margin-bottom:8px}
.login__remember span{width:8px;height:8px;border:1px solid var(--muted)}
.login__btn{display:inline-block;background:var(--green);color:#fff;font-size:8px;font-weight:600;padding:4px 12px}
.hero__title{left:110px;top:236px;background:var(--blue);color:#fff;font-size:34px;font-weight:800;padding:2px 12px;text-transform:uppercase}
.hero__sub{left:110px;top:290px;width:440px;color:#fff;font-size:20px;font-weight:700;line-height:26px;text-transform:uppercase}
.hero__actions{left:110px;top:356px;display:flex;gap:14px}

/* partners */
.partners{left:0;top:535px;width:1200px;height:95px;background:#f1f2f4;display:flex;justify-content:center;gap:120px;align-items:center}
.partner{height:56px;background:#d0d4dc}
.partner--round{width:56px;border-radius:50%;background:#9aa0b8}
.partner--wide{width:110px;border-radius:4px;background:#b4c7e8}
.partner--block{width:120px;border-radius:4px;background:#c7cde0}
.partner--food{width:110px;border-radius:4px;background:#f3cf9b}

/* intro + features */
.intro__name{top:648px;font-size:30px;color:var(--blue)}
.intro__tag{left:0;width:1200px;top:690px;font-size:13px;font-weight:700;color:var(--green);text-align:center;text-transform:uppercase}
.intro__features{left:0;width:1200px;top:712px;font-size:13px;font-weight:700;text-align:center;text-transform:uppercase}
.intro__dot{left:595px;top:748px}
.features{left:250px;top:780px;width:700px;display:grid;grid-template-columns:repeat(4,1fr);row-gap:24px;column-gap:0}
.feature{height:172px;padding:10px 14px;border-right:1px solid var(--line);text-align:center}
.feature:nth-child(4n){border-right:none}
.feature:nth-child(-n+4){border-bottom:1px solid var(--line)}
.feature svg{display:block;margin:0 auto 10px}
.feature__name{font-size:11px;font-weight:600;margin-bottom:6px}
.feature__text{font-size:8px;line-height:12px;color:var(--muted);margin-bottom:10px}
.feature__links{display:flex;justify-content:space-between;font-size:8px;padding:0 6px}
.feature__links b{color:var(--blue);font-weight:600}
.feature__links span{color:var(--muted)}
.features__more{left:515px;top:1208px}

/* services */
.services{left:0;top:1250px;width:1200px;height:540px}
.services__title{top:120px;color:var(--white)}
.services__dot{left:595px;top:165px;background:var(--white)}
.service{top:200px;width:260px;text-align:center;color:var(--white)}
.service__badge{width:156px;height:156px;border-radius:50%;background:var(--white);margin:0 auto 24px;display:flex;align-items:center;justify-content:center;box-shadow:0 0 0 10px rgba(255,255,255,.25)}
.service__name{font-size:15px;font-weight:500;margin-bottom:8px}
.service__text{font-size:10px;line-height:15px;opacity:.9}

/* about */
.ring{border-radius:50%;border:38px solid var(--blue)}
.about__title{left:250px;top:2000px;font-size:30px;font-weight:700;color:var(--blue)}
.about__lead{left:250px;top:2040px;width:330px;font-size:17px;line-height:23px;color:#333}
.about__text{left:250px;top:2120px;width:300px;font-size:9px;line-height:13px;color:var(--muted)}
.about__btn{left:250px;top:2195px}
.about__photo{left:598px;top:1960px;width:346px;height:346px;border-radius:50%;background:linear-gradient(160deg,#cfd8ef 0%,#6c7aa0 55%,#2b3552 100%)}

/* pricing */
.pricing__bgphoto{left:840px;top:2380px;width:360px;height:640px;background:linear-gradient(180deg,rgba(230,232,236,0) 0%,#e6e8ec 40%,#d8dbe1 100%)}
.pricing__title{top:2392px}
.pricing__dot{left:595px;top:2440px}
.plan{top:2496px;width:220px;height:482px;background:var(--white);box-shadow:0 4px 16px rgba(0,0,0,.12);text-align:center}
.plan__photo{height:190px}
.plan__name{font-size:12px;font-weight:700;margin:14px 0 10px;text-transform:uppercase}
.plan__price{height:44px;color:#fff;font-size:30px;font-weight:700;line-height:44px}
.plan__price small{font-size:8px;font-weight:500}
.plan__list{list-style:none;font-size:9px;color:var(--muted);margin:12px 0}
.plan__list li{padding:5px 0;border-bottom:1px solid var(--line);margin:0 24px}
.plan--green .plan__price{background:var(--green)}
.plan--blue .plan__price{background:var(--blue)}
.plan--orange .plan__price{background:var(--orange)}

/* testimonials */
.testimonials{left:0;top:3046px;width:1200px;height:340px;background:linear-gradient(180deg,#141517,#2a2b2f)}
.testimonials__title{top:3088px;color:var(--white)}
.testimonials__dot{left:595px;top:3134px;background:var(--white)}
.quote{top:3181px;width:340px;height:135px;border:2px solid var(--green);background:rgba(0,0,0,.35);color:#fff;text-align:center;padding:14px 20px}
.quote__mark{font-size:34px;font-weight:700;line-height:26px}
.quote__text{font-size:9px;line-height:13px;margin:8px 0 10px;opacity:.9}
.quote__name{font-size:10px;font-weight:600}

/* blogs */
.blogs__ghost{left:0;width:1200px;top:3395px;font-size:130px;font-weight:800;letter-spacing:40px;color:#f1f2f5;text-align:center}
.blogs__title{top:3432px}
.blogs__dot{left:595px;top:3478px}
.blog__img{border-radius:18px}
.blog__date{font-size:9px;color:var(--muted)}
.blog__title{font-size:13px;font-weight:700;line-height:17px;margin:6px 0}
.blog__text{font-size:8px;line-height:12px;color:var(--muted)}
.blog__more{font-size:8px;font-weight:700;margin-top:6px}

/* faq */
.faq__title{top:3970px}
.faq__dot{left:595px;top:4016px}
.faq-item{width:346px;min-height:32px;background:var(--white);box-shadow:0 2px 8px rgba(0,0,0,.1);font-size:10px;padding:9px 14px;display:flex;gap:10px;color:#333}
.faq-item--open{background:var(--blue);color:#fff;display:block;padding:10px 14px}
.faq-item--open p{font-size:8px;line-height:12px;margin-top:6px;opacity:.95}
.faq-item strong{font-weight:600}

/* contact */
.contact{left:0;top:4230px;width:1200px;height:482px}
.contact__title{top:4380px;color:var(--white)}
.contact__text{left:400px;top:4425px;width:400px;text-align:center;color:#fff;font-size:12px;line-height:17px;opacity:.9}
.contact__input{left:425px;top:4488px;width:350px;height:36px;background:#fff;font-size:10px;color:var(--muted);padding:11px 14px}
.contact__btn{left:555px;top:4544px}
.contact__info{left:330px;top:4606px;width:560px;display:flex;justify-content:space-between;color:#fff;font-size:9px}
.contact__info span{display:flex;align-items:center;gap:5px}
.footer__social{left:250px;top:4664px;display:flex;gap:6px}
.footer__social span{width:16px;height:16px;border-radius:50%;background:#fff}
.footer__copy{left:700px;top:4662px;width:250px;text-align:right;color:#fff;font-size:8px;line-height:11px}
</style>
</head>
<body>

<!-- HERO -->
<div class="abs hero" role="img" aria-label="Photo of a businessman working with a phone and laptop at a desk"></div>
<svg class="abs hero__corner" width="1200" height="535" viewBox="0 0 1200 535">
  <path d="M0 0H420L300 45 0 60Z" fill="#1d5cf0"/>
  <path d="M960 0H1200V140Z" fill="#1d5cf0"/>
  <path d="M0 40H1200V0H0Z" fill="rgba(20,20,25,.35)"/>
</svg>
<div class="abs brand">TaskGrid360</div>
<nav class="abs menu"><span>Home</span><span>About us</span><span>Services</span><span>Features ▾</span><span>Pricing</span><span>FAQ</span><span>Contact us</span></nav>
<div class="abs menu__cta">My Account</div>
<div class="abs login">
  <div class="login__field"></div>
  <div class="login__field"></div>
  <div class="login__remember"><span></span>Remember me</div>
  <div class="login__btn">LOGIN</div>
</div>
<div class="abs hero__title">Business Software</div>
<div class="abs hero__sub">Lorem Ipsum is simply dummy text of the printing and typesetting industry</div>
<div class="abs hero__actions"><span class="btn btn--dark">Read more</span><span class="btn btn--green">Login</span></div>

<!-- PARTNERS -->
<div class="abs partners">
  <div class="partner partner--round"></div>
  <div class="partner partner--wide"></div>
  <div class="partner partner--block"></div>
  <div class="partner partner--food"></div>
</div>

<!-- INTRO + FEATURES -->
<div class="abs section-title intro__name">TaskGrid360</div>
<div class="abs intro__tag">Business and Law Enforcement</div>
<div class="abs intro__features">Features</div>
<div class="abs dot intro__dot"></div>

<div class="abs features">
  <div class="feature">
    <svg width="44" height="40" viewBox="0 0 44 40" fill="none" stroke="#1d5cf0" stroke-width="2"><rect x="3" y="4" width="38" height="26" rx="2"/><path d="M22 30v6M12 36h20M9 22l8-8 6 6 10-10"/></svg>
    <div class="feature__name">Bulletin Board</div>
    <div class="feature__text">Communicate with all your locations and team members in one place, share documents</div>
    <div class="feature__links"><b>Read more</b><span>Get free trial</span></div>
  </div>
  <div class="feature">
    <svg width="44" height="40" viewBox="0 0 44 40" fill="none" stroke="#1d5cf0" stroke-width="2"><rect x="4" y="6" width="36" height="30" rx="2"/><path d="M4 14h36M12 2v8M32 2v8M12 21h4M20 21h4M28 21h4M12 28h4M20 28h4"/></svg>
    <div class="feature__name">Team Scheduling</div>
    <div class="feature__text">Build your shift schedule in minutes for multiple teams and locations at once</div>
    <div class="feature__links"><b>Read more</b><span>Get free trial</span></div>
  </div>
  <div class="feature">
    <svg width="44" height="40" viewBox="0 0 44 40" fill="none" stroke="#1d5cf0" stroke-width="2"><circle cx="22" cy="10" r="5"/><circle cx="9" cy="18" r="4"/><circle cx="35" cy="18" r="4"/><path d="M13 34c0-6 4-10 9-10s9 4 9 10M2 32c0-4 3-7 7-7M42 32c0-4-3-7-7-7"/></svg>
    <div class="feature__name">Team Training</div>
    <div class="feature__text">Offer a single place for team members to access training and track progress</div>
    <div class="feature__links"><b>Read more</b><span>Get free trial</span></div>
  </div>
  <div class="feature">
    <svg width="44" height="40" viewBox="0 0 44 40" fill="none" stroke="#1d5cf0" stroke-width="2"><circle cx="22" cy="12" r="6"/><path d="M10 36c0-8 5-13 12-13s12 5 12 13M6 10h6M32 10h6M22 1v4"/></svg>
    <div class="feature__name">Human Resources</div>
    <div class="feature__text">Store your staff records and documents securely, all searchable from one desk</div>
    <div class="feature__links"><b>Read more</b><span>Get free trial</span></div>
  </div>
  <div class="feature">
    <svg width="44" height="40" viewBox="0 0 44 40" fill="none" stroke="#1d5cf0" stroke-width="2"><rect x="4" y="14" width="20" height="22" rx="2"/><path d="M9 14V9h10v5M28 10l10 10M36 8l4 4-10 10-4-4z"/></svg>
    <div class="feature__name">Equipment Tracking</div>
    <div class="feature__text">Know where every piece of gear is, who has it and when it needs a service</div>
    <div class="feature__links"><b>Read more</b><span>Get free trial</span></div>
  </div>
  <div class="feature">
    <svg width="44" height="40" viewBox="0 0 44 40" fill="none" stroke="#1d5cf0" stroke-width="2"><rect x="6" y="4" width="32" height="32" rx="2"/><path d="M12 14h20M12 21h20M12 28h12"/></svg>
    <div class="feature__name">Extra Work</div>
    <div class="feature__text">Post extra shifts and overtime, let staff sign up and approve them in one click</div>
    <div class="feature__links"><b>Read more</b><span>Get free trial</span></div>
  </div>
  <div class="feature">
    <svg width="44" height="40" viewBox="0 0 44 40" fill="none" stroke="#1d5cf0" stroke-width="2"><path d="M4 26V16l6-6h14v16M24 16h8l8 6v4H4"/><circle cx="12" cy="30" r="4"/><circle cx="32" cy="30" r="4"/></svg>
    <div class="feature__name">Fleet Management</div>
    <div class="feature__text">Keep vehicles on the road with mileage logs, service dates and damage reports</div>
    <div class="feature__links"><b>Read more</b><span>Get free trial</span></div>
  </div>
  <div class="feature">
    <svg width="44" height="40" viewBox="0 0 44 40" fill="none" stroke="#1d5cf0" stroke-width="2"><path d="M22 3l16 8v18l-16 8-16-8V11z"/><path d="M6 11l16 8 16-8M22 19v18"/></svg>
    <div class="feature__name">Product Tracking</div>
    <div class="feature__text">Follow stock levels and orders across sites with simple alerts and reports</div>
    <div class="feature__links"><b>Read more</b><span>Get free trial</span></div>
  </div>
</div>
<div class="abs btn btn--green features__more">Law enforcement view more</div>

<!-- SERVICES -->
<svg class="abs services" width="1200" height="540" viewBox="0 0 1200 540">
  <defs><linearGradient id="svcGrad" x1="0" y1="0" x2="1" y2="1"><stop offset="0" stop-color="#1d5cf0"/><stop offset="1" stop-color="#0f3fc4"/></linearGradient></defs>
  <path d="M0 70C200 10 420 0 600 60S1000 120 1200 20V470C1000 520 820 440 640 470S220 560 0 500Z" fill="url(#svcGrad)"/>
  <path d="M0 500C220 560 420 470 640 470S1000 520 1200 470V500C1000 540 820 480 640 500S220 590 0 530Z" fill="#c7d5fa"/>
  <circle cx="1060" cy="200" r="90" fill="rgba(255,255,255,.05)"/>
  <circle cx="140" cy="380" r="60" fill="rgba(255,255,255,.05)"/>
</svg>
<div class="abs section-title services__title" style="top:1370px">Our Services</div>
<div class="abs dot services__dot" style="top:1415px"></div>
<div class="abs service" style="left:225px;top:1450px">
  <div class="service__badge"><svg width="70" height="70" viewBox="0 0 70 70" fill="none" stroke="#1d5cf0" stroke-width="3"><circle cx="35" cy="35" r="12"/><circle cx="35" cy="35" r="4" fill="#1d5cf0"/><path d="M35 8v10M35 52v10M8 35h10M52 35h10M16 16l7 7M47 47l7 7M54 16l-7 7M23 47l-7 7"/></svg></div>
  <div class="service__name">Strategy &amp; Planning</div>
  <div class="service__text">Lorem Ipsum is simply dummy text of the printing and typesetting industry. Lorem Ipsum has been the industry's.</div>
</div>
<div class="abs service" style="left:470px;top:1450px">
  <div class="service__badge"><svg width="70" height="70" viewBox="0 0 70 70" fill="none" stroke="#1d5cf0" stroke-width="3"><rect x="12" y="12" width="46" height="40" rx="3"/><path d="M20 42l10-12 8 8 12-14M24 60h22"/></svg></div>
  <div class="service__name">Branding &amp; Campaigns</div>
  <div class="service__text">Lorem Ipsum is simply dummy text of the printing and typesetting industry. Lorem Ipsum has been the industry's.</div>
</div>
<div class="abs service" style="left:715px;top:1450px">
  <div class="service__badge"><svg width="70" height="70" viewBox="0 0 70 70" fill="none" stroke="#1d5cf0" stroke-width="3"><rect x="22" y="8" width="26" height="52" rx="4"/><path d="M31 52h8M28 20h14M28 28h14M28 36h8"/></svg></div>
  <div class="service__name">Web &amp; Mobile</div>
  <div class="service__text">Lorem Ipsum is simply dummy text of the printing and typesetting industry. Lorem Ipsum has been the industry's.</div>
</div>

<!-- ABOUT -->
<div class="abs" style="left:0;top:1760px;width:230px;height:230px;border-radius:50%;background:#f2f4f8"></div>
<div class="abs ring" style="left:-80px;top:1865px;width:170px;height:170px"></div>
<div class="abs about__title">ABOUT US</div>
<div class="abs about__lead">Lorem Ipsum is simply dummy text of the printing and typesetting industry. Lorem Ipsum has been the industry's</div>
<div class="abs about__text">Lorem Ipsum is simply dummy text of the printing and typesetting industry. Lorem Ipsum has been the industry's standard dummy text ever since the 1500s, when an unknown printer took a galley of type and scrambled it to make a type specimen book.</div>
<div class="abs btn btn--blue about__btn">Read more</div>
<div class="abs" style="left:590px;top:1952px;width:362px;height:362px;border-radius:50%;background:#e4eafb"></div>
<div class="abs about__photo" role="img" aria-label="Photo of a team celebrating success in a meeting room"></div>

<!-- PRICING -->
<div class="abs pricing__bgphoto" role="img" aria-label="Faded photo of a businessman in a suit"></div>
<div class="abs section-title pricing__title">Our Pricing</div>
<div class="abs dot pricing__dot"></div>
<div class="abs plan plan--green" style="left:251px">
  <div class="plan__photo" role="img" aria-label="Illustration of a small team building a puzzle" style="background:linear-gradient(135deg,#3b5fd6,#8fa8f0 60%,#f1c36b)"></div>
  <div class="plan__name">Small Team</div>
  <div class="plan__price">39$<small>/MONTH</small></div>
  <ul class="plan__list"><li>50 Patform</li><li>Free System updates</li><li>Email and Chat Support</li><li>No Contracts</li><li>SSL Security</li><li>30 Day Money Back Guarantee</li></ul>
  <span class="btn btn--green">Try it free</span>
</div>
<div class="abs plan plan--blue" style="left:490px">
  <div class="plan__photo" role="img" aria-label="Photo of a desk with charts, calculator and laptop" style="background:linear-gradient(135deg,#2a6cd8,#9cc3e8 50%,#e8b44c)"></div>
  <div class="plan__name">Medium Team</div>
  <div class="plan__price">79$<small>/MONTH</small></div>
  <ul class="plan__list"><li>100 Patform</li><li>Free System updates</li><li>Email and Chat Support</li><li>No Contracts</li><li>SSL Security</li><li>30 Day Money Back Guarantee</li></ul>
  <span class="btn btn--blue">Try it free</span>
</div>
<div class="abs plan plan--orange" style="left:729px">
  <div class="plan__photo" role="img" aria-label="Photo of business partners shaking hands" style="background:linear-gradient(135deg,#1d7c7a,#6fb6c0 50%,#d7e4e6)"></div>
  <div class="plan__name">Large Team</div>
  <div class="plan__price">159$<small>/MONTH</small></div>
  <ul class="plan__list"><li>200 Patform</li><li>Free System updates</li><li>Email and Chat Support</li><li>No Contracts</li><li>SSL Security</li><li>30 Day Money Back Guarantee</li></ul>
  <span class="btn btn--orange">Try it free</span>
</div>

<!-- TESTIMONIALS -->
<div class="abs testimonials" role="img" aria-label="Dark photo of an office meeting behind testimonials"></div>
<div class="abs section-title testimonials__title">Testimonials</div>
<div class="abs dot testimonials__dot"></div>
<div class="abs quote" style="left:254px">
  <div class="quote__mark">“</div>
  <div class="quote__text">Lorem Ipsum is simply dummy text of the printing and typesetting industry. Lorem Ipsum has been the industry's standard dummy text ever since the 1500s, when an unknown printer took a galley of type and scrambled it.</div>
  <div class="quote__name">SAM RIVERA</div>
</div>
<div class="abs quote" style="left:606px">
  <div class="quote__mark">“</div>
  <div class="quote__text">Lorem Ipsum is simply dummy text of the printing and typesetting industry. Lorem Ipsum has been the industry's standard dummy text ever since the 1500s, when an unknown printer took a galley of type and scrambled it.</div>
  <div class="quote__name">SAM RIVERA</div>
</div>

<!-- BLOGS -->
<div class="abs blogs__ghost">BLOGS</div>
<div class="abs ring" style="left:1040px;top:3400px;width:420px;height:560px;border-width:60px"></div>
<div class="abs section-title blogs__title">Latest Blogs</div>
<div class="abs dot blogs__dot"></div>
<div class="abs blog__img" style="left:256px;top:3542px;width:232px;height:180px;background:linear-gradient(135deg,#c9b49a,#7e8fa6)" role="img" aria-label="Photo of a team working around a table with papers"></div>
<div class="abs blog__img" style="left:496px;top:3535px;width:232px;height:200px;background:linear-gradient(135deg,#d9cfc2,#8b7b6a)" role="img" aria-label="Photo of colleagues smiling at a laptop"></div>
<div class="abs" style="left:740px;top:3560px;width:205px">
  <div class="blog__date">20 September 2018</div>
  <div class="blog__title">LOREM IPSUM IS SIMPLY DUMMY TEXT OF THE PRINTING</div>
  <div class="blog__text">Lorem Ipsum is simply dummy text of the printing and typesetting industry. Lorem Ipsum has been the industry's standard dummy text ever since the 1500s, when an unknown printer took a galley.</div>
  <div class="blog__more">READ MORE</div>
</div>
<div class="abs" style="left:256px;top:3735px;width:225px">
  <div class="blog__date">19 September 2018</div>
  <div class="blog__title">LOREM IPSUM IS SIMPLY DUMMY TEXT OF THE PRINTING</div>
  <div class="blog__text">Lorem Ipsum is simply dummy text of the printing and typesetting industry. Lorem Ipsum has been the industry's standard dummy text ever since the 1500s, when an unknown printer took a galley.</div>
  <div class="blog__more">READ MORE</div>
</div>
<div class="abs blog__img" style="left:496px;top:3745px;width:232px;height:170px;background:linear-gradient(135deg,#b9c4cf,#5e6a78)" role="img" aria-label="Photo of a business meeting in an office"></div>
<div class="abs" style="left:740px;top:3760px;width:205px">
  <div class="blog__date">20 September 2018</div>
  <div class="blog__title">LOREM IPSUM IS SIMPLY DUMMY TEXT OF THE PRINTING</div>
  <div class="blog__text">Lorem Ipsum is simply dummy text of the printing and typesetting industry. Lorem Ipsum has been the industry's standard dummy text ever since the 1500s, when an unknown printer took a galley.</div>
  <div class="blog__more">READ MORE</div>
</div>

<!-- FAQ -->
<div class="abs section-title faq__title">FAQ's</div>
<div class="abs dot faq__dot"></div>
<div class="abs faq-item" style="left:251px;top:4066px"><strong>01</strong> What is Lorem Ipsum?</div>
<div class="abs faq-item faq-item--open" style="left:251px;top:4110px"><strong>02</strong>&nbsp; Lorem Ipsum is simply dummy text of the printing<p>Lorem Ipsum is simply dummy text of the printing and typesetting industry. Lorem Ipsum has been the industry's standard dummy text ever since the 1500s, when an unknown printer took a galley of type.</p></div>
<div class="abs faq-item" style="left:606px;top:4066px"><strong>03</strong> Lorem Ipsum is simply dummy text of the printing</div>
<div class="abs faq-item" style="left:606px;top:4110px"><strong>04</strong> What is Lorem Ipsum?</div>
<div class="abs faq-item" style="left:606px;top:4154px"><strong>05</strong> LOREM IPSUM IS SIMPLY DUMMY TEXT OF THE PRINTING</div>

<!-- CONTACT -->
<svg class="abs contact" width="1200" height="482" viewBox="0 0 1200 482">
  <defs><linearGradient id="ctGrad" x1="0" y1="0" x2="0" y2="1"><stop offset="0" stop-color="#3a78f5"/><stop offset="1" stop-color="#1d5cf0"/></linearGradient></defs>
  <path d="M0 150C150 60 260 40 420 70L900 20 1200 90V482H0Z" fill="#a9c2fa"/>
  <path d="M0 170C180 90 300 80 460 110S900 60 1200 120V482H0Z" fill="url(#ctGrad)"/>
</svg>
<div class="abs section-title contact__title">Contact Us</div>
<div class="abs contact__text">Lorem Ipsum is simply dummy text of the printing and typesetting industry. Lorem Ipsum has been the industry's</div>
<div class="abs contact__input">Your Email Address</div>
<div class="abs btn btn--orange contact__btn" style="padding:10px 36px">Sign up</div>
<div class="abs contact__info">
  <span><svg width="10" height="12" viewBox="0 0 10 12"><path d="M5 0a4 4 0 014 4c0 3-4 8-4 8S1 7 1 4a4 4 0 014-4z" fill="#fff"/></svg>48 Harbor Lane, Westfield #12</span>
  <span><svg width="11" height="11" viewBox="0 0 11 11"><path d="M2 0l2 3-1 1.5c.7 1.5 2 2.8 3.5 3.5L8 7l3 2-1 2C5 11 0 6 0 1z" fill="#fff"/></svg>Office: 555 010 2244</span>
  <span><svg width="12" height="9" viewBox="0 0 12 9"><rect width="12" height="9" fill="#fff"/><path d="M0 0l6 5 6-5" stroke="#1d5cf0" fill="none"/></svg>Email: info@taskgrid-demo.com</span>
</div>
<div class="abs footer__social"><span></span><span></span><span></span><span></span><span></span><span></span></div>
<div class="abs footer__copy">Copyright © 2018 <b>Business Software</b>. All Right Reserved</div>

</body>
</html>
```